Physiotherapiepraxis braucht Druckvorlage für Werbeanzeige
Zielgruppe
Dienstleistung im Gesundheitswesen als Physiotherapiepraxis.
Krankengymnastik, auch im häuslichen Bereich oder im Altersheim, und Massage sowie Wellnessanwendungen.
Zielgruppe sind primär Erwachsene, eingeschränkt auch Kinder.
Aufgabenstellung
Ich möchte eine Druckvorlage für eine Werbeanzeige, die ich immer mal wieder in verschiedenen Festschriften im dörflichen Bereich oder in einer regionalen Zeitschrift veröffentlichen kann.
Die Anzeige soll das Logo enthalten und die Anschrift der Praxis sowie die Telefonnummer und Adresse der Homepage.

```html
<!DOCTYPE html>
<html lang="de">
<head>
<meta charset="utf-8">
<title>Anzeigen 1-spaltig – Physiotherapie Helene Albers</title>
<link href="https://fonts.googleapis.com/css2?family=Source+Sans+3:wght@400;600;700&family=Caveat:wght@600&display=swap" rel="stylesheet">
<style>
  :root{
    --yellow:#d4b822;
    --green:#007a3b;
    --grey-dark:#565656;
    --grey-light:#b1b1b1;
    --white:#ffffff;
    --caption:#555555;
  }
  *{box-sizing:border-box;margin:0;padding:0}
  html,body{width:1200px;height:846px;overflow:hidden;background:var(--white)}
  body{position:relative;font-family:"Source Sans 3",sans-serif}
  .sheet-title{position:absolute;left:143px;top:41px;font-size:22px;font-weight:400;color:var(--caption)}

  .ad{position:absolute;width:257px;height:257px;border:1px solid var(--main);background:var(--white);overflow:hidden}
  .ad--yellow{--main:var(--yellow);--badge:var(--green);--name:var(--green);--dot:var(--yellow);--slogan:var(--green)}
  .ad--green{--main:var(--green);--badge:var(--yellow);--name:var(--green);--dot:var(--yellow);--slogan:var(--yellow)}
  .ad--grey{--main:var(--grey-dark);--badge:var(--grey-light);--name:var(--grey-dark);--dot:var(--grey-light);--slogan:var(--grey-dark)}

  .col-1{left:142px}.col-2{left:471px}.col-3{left:800px}
  .row-1{top:81px}.row-2{top:495px}

  .contact{background:var(--main);color:var(--white);padding:5px 14px 0;font-size:14.5px;line-height:18.5px}
  .contact .practice{font-weight:700;letter-spacing:.2px}
  .contact .detail{font-weight:400}
  .contact .address{margin-top:3px}

  .ad--top .contact{height:85px}
  .badge{position:absolute;right:12px;top:75px;transform:rotate(-6deg);background:var(--badge);color:var(--white);
    border:2px solid var(--white);border-radius:8px;padding:2px 10px 3px;font-family:"Caveat",cursive;font-size:19px;line-height:17px;text-align:right;box-shadow:0 0 0 0 transparent}
  .web{position:absolute;left:0;right:0;bottom:0;height:23px;background:var(--main);color:var(--white);
    font-weight:700;font-size:14.5px;line-height:23px;padding-left:14px}

  .brand{position:absolute;left:0;right:0;display:flex;align-items:center;justify-content:center;gap:10px;color:var(--name)}
  .brand .dot{width:12px;height:12px;border-radius:50%;background:var(--dot);flex:none}
  .brand .name{font-weight:600;font-size:21px;line-height:24px;letter-spacing:1.5px;text-align:center}
  .ad--top .brand{top:146px}
  .ad--bottom .brand{top:62px}

  .slogan{position:absolute;left:0;right:0;top:10px;text-align:center;font-family:"Caveat",cursive;font-size:21px;color:var(--slogan)}
  .ad--bottom .contact{position:absolute;left:0;right:0;bottom:0;height:109px;padding-top:4px}
  .ad--bottom .contact .web-line{font-weight:700;margin-top:3px}
</style>
</head>
<body>
  <h1 class="sheet-title">Anzeigen 1-spaltig, 45 mm breit</h1>

  <article class="ad ad--top ad--yellow col-1 row-1">
    <div class="contact">
      <p class="practice">Praxis für Physiotherapie<br>Helene Albers</p>
      <p class="detail address">Lindenweg 7, 24591 Hollerbek</p>
      <p class="detail">Tel. 04281 - 37 62 15</p>
    </div>
    <p class="badge">Wir bringen Sie<br>gerne in Bewegung!</p>
    <div class="brand"><span class="dot"></span><p class="name">Helene Albers<br>Physiotherapie</p></div>
    <p class="web">www.physiotherapie-hollerbek.de</p>
  </article>

  <article class="ad ad--top ad--green col-2 row-1">
    <div class="contact">
      <p class="practice">Praxis für Physiotherapie<br>Helene Albers</p>
      <p class="detail address">Lindenweg 7, 24591 Hollerbek</p>
      <p class="detail">Tel. 04281 - 37 62 15</p>
    </div>
    <p class="badge">Wir bringen Sie<br>gerne in Bewegung!</p>
    <div class="brand"><span class="dot"></span><p class="name">Helene Albers<br>Physiotherapie</p></div>
    <p class="web">www.physiotherapie-hollerbek.de</p>
  </article>

  <article class="ad ad--top ad--grey col-3 row-1">
    <div class="contact">
      <p class="practice">Praxis für Physiotherapie<br>Helene Albers</p>
      <p class="detail address">Lindenweg 7, 24591 Hollerbek</p>
      <p class="detail">Tel. 04281 - 37 62 15</p>
    </div>
    <p class="badge">Wir bringen Sie<br>gerne in Bewegung!</p>
    <div class="brand"><span class="dot"></span><p class="name">Helene Albers<br>Physiotherapie</p></div>
    <p class="web">www.physiotherapie-hollerbek.de</p>
  </article>

  <article class="ad ad--bottom ad--yellow col-1 row-2">
    <p class="slogan">Wir bringen Sie gerne in Bewegung!</p>
    <div class="brand"><span class="dot"></span><p class="name">Helene Albers<br>Physiotherapie</p></div>
    <div class="contact">
      <p class="practice">Praxis für Physiotherapie<br>Helene Albers</p>
      <p class="detail address">Lindenweg 7, 24591 Hollerbek</p>
      <p class="detail">Tel. 04281 - 37 62 15</p>
      <p class="web-line">www.physiotherapie-hollerbek.de</p>
    </div>
  </article>

  <article class="ad ad--bottom ad--green col-2 row-2">
    <p class="slogan">Wir bringen Sie gerne in Bewegung!</p>
    <div class="brand"><span class="dot"></span><p class="name">Helene Albers<br>Physiotherapie</p></div>
    <div class="contact">
      <p class="practice">Praxis für Physiotherapie<br>Helene Albers</p>
      <p class="detail address">Lindenweg 7, 24591 Hollerbek</p>
      <p class="detail">Tel. 04281 - 37 62 15</p>
      <p class="web-line">www.physiotherapie-hollerbek.de</p>
    </div>
  </article>

  <article class="ad ad--bottom ad--grey col-3 row-2">
    <p class="slogan">Wir bringen Sie gerne in Bewegung!</p>
    <div class="brand"><span class="dot"></span><p class="name">Helene Albers<br>Physiotherapie</p></div>
    <div class="contact">
      <p class="practice">Praxis für Physiotherapie<br>Helene Albers</p>
      <p class="detail address">Lindenweg 7, 24591 Hollerbek</p>
      <p class="detail">Tel. 04281 - 37 62 15</p>
      <p class="web-line">www.physiotherapie-hollerbek.de</p>
    </div>
  </article>
</body>
</html>
```